Coffee Shop needs a fresh new menu

Hi,
I would like a new menu to be designed for our coffee shop.
We display our menu on a television screen, so would need it in a file that would allow us to continue to do so -- I have attached a photo so that you can see our current design, and how it is displayed.

I'd like something that is easy to read, if the design could have a "hipster" feel to it -- we are located at a hospital and University.

I have attached a Word file with what we would like on the menu.

Feel free to contact me if you have any questions.

Thanks,
Tam

Just A4 size will be fine, and no need to include menu 1 and menu 2 - I just put them in as an example of what we already have -- they are our printed menu's. Thanks

Hospital

```html
<!DOCTYPE html>
<html lang="en">
<head>
<meta charset="utf-8">
<title>Focaccias &amp; Wraps Menu</title>
<link rel="stylesheet" href="https://fonts.googleapis.com/css2?family=Playfair+Display:ital,wght@0,800;1,800&family=Figtree:wght@600;700&display=swap">
<style>
  :root {
    --paper: #ede8d7;
    --paper-edge: #e4dec9;
    --ink: #141210;
    --ingredient-red: #e2382b;
    --ingredient-green: #1f9a4c;
    --flourish-tone: rgba(120, 112, 96, 0.12);
  }
  * { margin: 0; padding: 0; box-sizing: border-box; }
  html, body { width: 849px; height: 1200px; overflow: hidden; }
  body {
    background: radial-gradient(ellipse at 40% 40%, var(--paper) 60%, var(--paper-edge) 100%);
    font-family: "Figtree", Arial, sans-serif;
    color: var(--ink);
    position: relative;
  }
  .menu-section { position: absolute; left: 0; width: 849px; }
  .section-focaccias { top: 0; }
  .section-wraps { top: 516px; }

  .flourish {
    position: absolute;
    border-radius: 50%;
    background: radial-gradient(ellipse at center, var(--flourish-tone) 0%, rgba(120,112,96,0) 70%);
  }
  .section-focaccias .flourish { left: 45px; top: 92px; width: 220px; height: 150px; }
  .section-wraps .flourish { left: 112px; top: 102px; width: 170px; height: 100px; }

  .section-title {
    position: absolute;
    font-family: "Playfair Display", "Times New Roman", serif;
    font-weight: 800;
    font-size: 60px;
    line-height: 1;
    letter-spacing: -0.5px;
  }
  .section-focaccias .section-title { left: 117px; top: 118px; }
  .section-wraps .section-title { left: 119px; top: 126px; font-size: 58px; }

  .section-note {
    position: absolute;
    left: 123px;
    font-weight: 700;
    font-size: 16px;
    line-height: 24px;
  }
  .section-focaccias .section-note { top: 198px; }
  .section-wraps .section-note { top: 198px; }

  .item-grid {
    position: absolute;
    left: 123px;
    top: 283px;
    display: grid;
    grid-template-columns: 311px 200px;
    grid-auto-rows: 84px;
    grid-auto-flow: column;
  }
  .section-focaccias .item-grid { grid-template-rows: repeat(4, 84px); }
  .section-wraps .item-grid { top: 283px; grid-template-rows: repeat(4, 84px); }
  .item-name { font-weight: 700; font-size: 17px; line-height: 22px; }
  .item-ingredients {
    margin-top: 5px;
    font-weight: 600;
    font-size: 9.6px;
    line-height: 12px;
    color: var(--ingredient-red);
    width: 190px;
  }
  .item-vegetarian .item-ingredients { color: var(--ingredient-green); }
  .item-empty { visibility: hidden; }
</style>
</head>
<body>
  <section class="menu-section section-focaccias">
    <div class="flourish" role="img" aria-label="Decorative flourish swirl behind the heading"></div>
    <h1 class="section-title">focaccias</h1>
    <p class="section-note">Toasted and Cut into Two<br>$ 7.50 Each</p>
    <div class="item-grid">
      <div class="item"><h2 class="item-name">Chicken Schnitzel</h2><p class="item-ingredients">Butter, Mayo, Lettuce, Cheese, Tomato and Schnitzel</p></div>
      <div class="item"><h2 class="item-name">Salami</h2><p class="item-ingredients">Butter, Pesto, Spinach, Salami Roast Capsicum, Feta, Olives and Salami</p></div>
      <div class="item"><h2 class="item-name">Chicken &amp; Avocado</h2><p class="item-ingredients">Butter, Mayo, Lettuce, Cheese, Tomato, Chicken and Avocado</p></div>
      <div class="item item-empty"></div>
      <div class="item"><h2 class="item-name">Ham</h2><p class="item-ingredients">Butter, Pickle Spread, Cheese, Tomato and Ham</p></div>
      <div class="item"><h2 class="item-name">Sweet Chili Chicken</h2><p class="item-ingredients">Butter, Sweet Chili Sauce, Spinach, Chicken Tenders, Cheese and Tomato</p></div>
      <div class="item item-vegetarian"><h2 class="item-name">Roast Vegetables</h2><p class="item-ingredients">Butter, Pesto, Spinach, Roast Eggplant, Zucchini, Capsicum and Feta</p></div>
      <div class="item"><h2 class="item-name">Roast Beef</h2><p class="item-ingredients">Butter, Dijon, Spinach, Beef, Cheese and Tomato</p></div>
    </div>
  </section>

  <section class="menu-section section-wraps">
    <div class="flourish" role="img" aria-label="Decorative flourish swirl behind the heading"></div>
    <h1 class="section-title">wraps</h1>
    <p class="section-note">Cut into Three<br>$ 7.50 Each</p>
    <div class="item-grid">
      <div class="item"><h2 class="item-name">Chicken Schnitzel</h2><p class="item-ingredients">Butter, Mayo, Lettuce, Cheese, Tomato and Schnitzel</p></div>
      <div class="item"><h2 class="item-name">Turkey</h2><p class="item-ingredients">Butter, Cranberry Sauce, Spinach, Tomato, Cucumber, Cheese and Turkey</p></div>
      <div class="item"><h2 class="item-name">Chicken &amp; Avocado</h2><p class="item-ingredients">Butter, Mayo, Lettuce, Cheese, Tomato, Chicken and Avocado</p></div>
      <div class="item"><h2 class="item-name">BLT</h2><p class="item-ingredients">Butter, Bacon, Lettuce and Tomato</p></div>
      <div class="item"><h2 class="item-name">Ham</h2><p class="item-ingredients">Butter, Pickle Spread, Cheese, Tomato and Ham</p></div>
      <div class="item"><h2 class="item-name">Sweet Chili Chicken</h2><p class="item-ingredients">Butter, Sweet Chili Sauce, Spinach, Chicken Tenders, Cheese and Tomato</p></div>
      <div class="item"><h2 class="item-name">Tandoori Chicken</h2><p class="item-ingredients">Butter, Tziki, Spinach, Tomato, Cucumber and Chicken</p></div>
      <div class="item item-vegetarian"><h2 class="item-name">Egg Mix</h2><p class="item-ingredients">Butter, Mayo, Lettuce and Egg</p></div>
    </div>
  </section>
</body>
</html>
```